Bluewater Products Flyer

Bluewater Lending Group, Inc.
Licensed Mortgage Company
Serving the DMV since 1997
"You choose Bluewater, we'll carry it home"
We specialize in...
FHA Loans
* Credit Scores as low as 500
* 203K Renovation Loans
Conventional Loans
* As little as 1% Down
* Bank Statement for Self-Employed
Investor Loans
* DSCR, & Fix & Flip
* Commercial & New Construction
Other Programs
* HELOCS & Reverse Mortgages
Call today for a free consultation
(800) 641-2957
www.bluewaterlendhub.com
NMLS #731846

```html
<!DOCTYPE html>
<html lang="en">
<head>
<meta charset="utf-8">
<title>Bluewater Products Flyer</title>
<link rel="stylesheet" href="https://fonts.googleapis.com/css2?family=Montserrat:wght@700;800&family=Open+Sans:wght@400;700;800&display=swap">
<style>
  :root {
    --page-bg: #d3d5e0;
    --white: #ffffff;
    --gold: #c38a3c;
    --gold-light: #f6cf86;
    --gold-dark: #9e6a2a;
    --navy: #1f3f8f;
    --navy-deep: #1b3479;
    --sky: #a9c3ea;
    --photo-warm: #d9cfc6;
    --photo-cool: #ecebee;
    --lawn: #6e8f44;
    --house: #b9b6a6;
  }
  * { margin: 0; padding: 0; box-sizing: border-box; }
  html, body { width: 1200px; height: 856px; overflow: hidden; background: var(--page-bg); }
  .flyer {
    position: absolute; left: 301px; top: 16px;
    width: 597px; height: 824px;
    background: var(--white);
    overflow: hidden;
    font-family: "Open Sans", sans-serif;
    box-shadow: 0 6px 18px rgba(40, 44, 70, .25);
  }
  .flyer-art { position: absolute; inset: 0; }
  .tagline { position: absolute; left: 15px; top: 290px; color: var(--gold); }
  .tagline-lead { font-family: "Open Sans", sans-serif; font-weight: 700; font-size: 18px; line-height: 1; }
  .tagline-name { font-family: "Montserrat", sans-serif; font-weight: 800; font-size: 44px; line-height: 1.05; letter-spacing: -.5px; }
  .tagline-close { font-family: "Open Sans", sans-serif; font-weight: 800; font-size: 18px; line-height: 1; }
  .specialize {
    position: absolute; left: 15px; top: 395px;
    font-family: "Open Sans", sans-serif; font-weight: 800; font-size: 25px;
    color: var(--navy);
  }
  .program-bar {
    position: absolute; left: 0; width: 237px; height: 33px;
    border-radius: 0 17px 17px 0;
    background: linear-gradient(90deg, var(--navy) 0%, #3d61ad 55%, var(--sky) 100%);
    color: var(--white);
    font-weight: 700; font-size: 15px; line-height: 33px; padding-left: 15px;
  }
  .program-point {
    position: absolute; left: 15px;
    font-weight: 700; font-size: 13px; color: var(--navy);
  }
  .program-point::before { content: "* "; }
  .brand-name {
    position: absolute; left: 400px; top: 368px; width: 190px;
    text-align: center;
    font-family: "Open Sans", sans-serif; font-weight: 800; font-size: 21px; line-height: 1.15;
    color: var(--navy);
  }
  .footer-call { position: absolute; left: 15px; top: 745px; color: var(--white); }
  .footer-call .call-note { font-size: 10px; font-weight: 400; }
  .footer-call .call-phone { font-family: "Open Sans", sans-serif; font-weight: 800; font-size: 26px; line-height: 1.05; }
  .footer-call .call-web { font-weight: 800; font-size: 16px; line-height: 1.3; white-space: nowrap; }
  .footer-license { position: absolute; left: 350px; top: 752px; color: var(--white); font-weight: 800; font-size: 13px; line-height: 1.05; }
  .footer-license .nmls { margin-top: 14px; }
</style>
</head>
<body>
<main class="flyer">
  <svg class="flyer-art" viewBox="0 0 597 824" width="597" height="824">
    <defs>
      <linearGradient id="familyTone" x1="0" y1="0" x2="1" y2="1">
        <stop offset="0" stop-color="var(--photo-cool)"/>
        <stop offset=".6" stop-color="var(--photo-warm)"/>
        <stop offset="1" stop-color="#b89880"/>
      </linearGradient>
      <linearGradient id="swoosh" x1="0" y1="0" x2="1" y2="1">
        <stop offset="0" stop-color="var(--gold-light)"/>
        <stop offset="1" stop-color="var(--gold)"/>
      </linearGradient>
      <linearGradient id="frameGold" x1="0" y1="0" x2="0" y2="1">
        <stop offset="0" stop-color="var(--gold)"/>
        <stop offset="1" stop-color="var(--gold-dark)"/>
      </linearGradient>
      <linearGradient id="homeTone" x1="0" y1="0" x2="0" y2="1">
        <stop offset="0" stop-color="var(--house)"/>
        <stop offset=".55" stop-color="#8a9a70"/>
        <stop offset="1" stop-color="var(--lawn)"/>
      </linearGradient>
      <linearGradient id="homeFade" x1="0" y1="0" x2="1" y2="0">
        <stop offset="0" stop-color="#fff" stop-opacity="1"/>
        <stop offset=".35" stop-color="#fff" stop-opacity="0"/>
      </linearGradient>
      <linearGradient id="footGold" x1="0" y1="0" x2="1" y2="1">
        <stop offset="0" stop-color="var(--gold-dark)"/>
        <stop offset=".6" stop-color="var(--gold)"/>
        <stop offset="1" stop-color="var(--gold-light)"/>
      </linearGradient>
      <linearGradient id="footNavy" x1="0" y1="0" x2="1" y2="0">
        <stop offset="0" stop-color="var(--navy-deep)"/>
        <stop offset=".6" stop-color="#3f64b0"/>
        <stop offset="1" stop-color="#c5daf3"/>
      </linearGradient>
    </defs>

    <path role="img" aria-label="Photo of a smiling family of four in white clothing" d="M0,0 H597 V316 H360 C210,260 25,200 0,25 Z" fill="url(#familyTone)"/>
    <path class="gold-swoosh" d="M0,25 C25,200 210,260 360,316 L400,345 C200,300 15,240 0,75 Z" fill="url(#swoosh)"/>

    <rect class="home-frame" x="420" y="474" width="177" height="266" fill="url(#frameGold)"/>
    <path role="img" aria-label="Photo of a cheering family in front of their new house holding a home for sale sign" d="M234,474 H540 C590,540 590,640 540,700 C520,720 500,735 480,740 H234 Z" fill="url(#homeTone)"/>
    <rect x="234" y="474" width="330" height="266" fill="url(#homeFade)"/>

    <path class="brand-panel" d="M470,313 H597 V477 H470 C410,477 392,440 392,395 C392,350 410,313 470,313 Z" fill="var(--white)"/>

    <path class="footer-gold" d="M0,740 H326 L278,824 H0 Z" fill="url(#footGold)"/>
    <path class="footer-navy" d="M334,740 H597 V824 H286 Z" fill="url(#footNavy)"/>
  </svg>

  <div class="tagline">
    <div class="tagline-lead">You choose</div>
    <div class="tagline-name">Bluewater,</div>
    <div class="tagline-close">we'll carry it home</div>
  </div>

  <div class="brand-name">Bluewater Lending Group</div>

  <h2 class="specialize">We specialize in...</h2>

  <div class="program-bar" style="top:430px">FHA Loans</div>
  <div class="program-point" style="top:466px">Credit Scores as low as 500</div>
  <div class="program-point" style="top:489px">203K Renovation Loans</div>

  <div class="program-bar" style="top:513px">Conventional Loans</div>
  <div class="program-point" style="top:549px">As little as 1% Down</div>
  <div class="program-point" style="top:572px">Bank Statement for Self-Employed</div>

  <div class="program-bar" style="top:596px">Investor Loans</div>
  <div class="program-point" style="top:633px">DSCR, &amp; Fix &amp; Flip</div>
  <div class="program-point" style="top:656px">Commercial &amp; New Construction</div>

  <div class="program-bar" style="top:680px">Other Programs</div>
  <div class="program-point" style="top:717px">HELOCS &amp; Reverse Mortgages</div>

  <div class="footer-call">
    <div class="call-note">Call today for a free consultation</div>
    <div class="call-phone">(800) 641-2957</div>
    <div class="call-web">www.bluewaterlendhub.com</div>
  </div>

  <div class="footer-license">
    <div>Licensed Mortgage Company</div>
    <div>Serving the DMV since 1997</div>
    <div class="nmls">NMLS #731846</div>
  </div>
</main>
</body>
</html>
```